PowerPoint Design Project

I need a Power Point slide template designed with 4 or 5 slides. We are a health care technology company and would like to take our current look and feel in this PP presentation to the next level and "prettied up"

Target Market(s)

Health Care Professionals

Industry/Entity Type

Health

Requirements
Must have
• Cannot change out the TREVONA logo. The logo is all CAPS
Should not have
• The color blue is restricted and cannot be used.

```html
<!DOCTYPE html>
<html lang="en">
<head>
<meta charset="utf-8">
<title>Our services – TREVONA</title>
<link rel="stylesheet" href="https://fonts.googleapis.com/css2?family=Arimo:wght@400;700&display=swap">
<style>
  :root {
    --brand-green: #aebd38;
    --accent-grey: #96989b;
    --text-grey: #5f5f5f;
    --subtitle-grey: #a3a3a3;
    --footer-grey: #8a8a8a;
    --wordmark-grey: #7f8184;
    --ornament-tint: rgba(150, 152, 155, 0.07);
    --page-white: #ffffff;
  }
  * { margin: 0; padding: 0; box-sizing: border-box; }
  html, body {
    width: 1200px;
    height: 900px;
    overflow: hidden;
    background: var(--page-white);
  }
  .slide {
    position: relative;
    width: 1200px;
    height: 900px;
    overflow: hidden;
    background: var(--page-white);
    font-family: "Arimo", Arial, sans-serif;
  }
  .background-ornament {
    position: absolute;
    left: 360px;
    top: 228px;
    width: 840px;
    height: 672px;
    border-radius: 320px 0 0 0;
    background: radial-gradient(ellipse at 55% 50%, var(--ornament-tint) 0%, rgba(150, 152, 155, 0.03) 55%, rgba(255, 255, 255, 0) 80%);
  }
  .title-band {
    position: absolute;
    left: 0;
    top: 40px;
    width: 1200px;
    height: 130px;
    background: var(--brand-green);
  }
  .corner-accent {
    position: absolute;
    left: 1010px;
    top: 0;
    width: 190px;
    height: 258px;
    border-radius: 0 0 0 90px;
    background: linear-gradient(135deg, #b9c64f 0%, var(--brand-green) 40%, var(--accent-grey) 75%);
  }
  .slide-title {
    position: absolute;
    left: 72px;
    top: 86px;
    font-size: 43px;
    font-weight: 400;
    color: var(--page-white);
    line-height: 1;
  }
  .section-subtitle {
    position: absolute;
    left: 72px;
    top: 209px;
    font-size: 34px;
    font-weight: 700;
    color: var(--subtitle-grey);
    line-height: 1;
  }
  .service-list {
    position: absolute;
    left: 72px;
    top: 291px;
    list-style: none;
  }
  .service-list li {
    position: relative;
    padding-left: 46px;
    font-size: 37px;
    line-height: 61px;
    color: var(--text-grey);
  }
  .service-list li::before {
    content: "";
    position: absolute;
    left: 4px;
    top: 29px;
    width: 8px;
    height: 8px;
    border-radius: 50%;
    background: var(--brand-green);
  }
  .slide-footer {
    position: absolute;
    left: 0;
    bottom: 0;
    width: 1200px;
    height: 60px;
  }
  .page-number {
    position: absolute;
    left: 36px;
    top: 8px;
    font-size: 14px;
    font-weight: 700;
    color: var(--text-grey);
  }
  .footer-rule {
    position: absolute;
    left: 70px;
    top: 6px;
    width: 1px;
    height: 54px;
    background: var(--brand-green);
  }
  .footer-note {
    position: absolute;
    left: 83px;
    top: 9px;
    font-size: 12.5px;
    color: var(--footer-grey);
  }
  .footer-note .company {
    font-weight: 700;
    color: var(--brand-green);
  }
  .wordmark {
    position: absolute;
    right: 34px;
    top: 832px;
    display: flex;
    align-items: center;
    gap: 12px;
  }
  .wordmark-square {
    width: 26px;
    height: 26px;
    background: var(--brand-green);
  }
  .wordmark-name {
    font-size: 36px;
    font-weight: 700;
    letter-spacing: 4px;
    color: var(--wordmark-grey);
    line-height: 1;
  }
</style>
</head>
<body>
  <div class="slide">
    <div class="background-ornament" role="img" aria-label="Faint large outlined brand emblem decoration"></div>
    <div class="title-band"></div>
    <div class="corner-accent" role="img" aria-label="Green and grey brand emblem corner decoration"></div>
    <h1 class="slide-title">Our services</h1>
    <h2 class="section-subtitle">What we do</h2>
    <ul class="service-list">
      <li>Services 1</li>
      <li>Services 2</li>
      <li>Services 3</li>
      <li>Services 4</li>
      <li>Services 5</li>
      <li>Services 6</li>
    </ul>
    <div class="wordmark">
      <span class="wordmark-square"></span>
      <span class="wordmark-name">TREVONA</span>
    </div>
    <footer class="slide-footer">
      <span class="page-number">3</span>
      <span class="footer-rule"></span>
      <span class="footer-note"><span class="company">TREVONA Network Inc</span> &nbsp;|&nbsp; Company Confidential</span>
    </footer>
  </div>
</body>
</html>
```